Gummy Label design for hemp company

I need a 3.25 inch wide by 4 inch tall label made to be put on bags of gummies. I will include all disclaimers that need to be there, as well as my logo. This is for our 25 mg Delta 8 gummies 20ct, but I will use the design for our entire gummy line, just editing the text. Needs to have ingredient list. Ingredients: Sugar, Inulin, Corn syrup, water, pectin, citric acid, baking soda, fruit, hemp extract.

Everything should be on one label as this is going on a sticker that will be placed on a bag.
I would like to highlight that they are vegan if possible.

• Must have the following disclaimer: "Contains Farm Bill compliant hemp extract. These statements have not been evaluated by the KWT. This product is NOT intended to treat, cure, or prevent any disease. Do not operate heavy machinery while using this product. This product may cause you to fail a drug test. Consult with your doctor before trying any new products. Do not take if pregnant or lactating. If you experience any adverse effects, discontinue use and seek advice from your physician."
• NEEDS TO SAY: "100% hemp derived" also "<.3% D9 THC"

```html
<!DOCTYPE html>
<html lang="en">
<head>
<meta charset="utf-8">
<title>Fernway Labs – Delta 8 Gummies Label Set</title>
<link rel="stylesheet" href="https://fonts.googleapis.com/css2?family=Montserrat:wght@400;500;700;800;900&display=swap">
<style>
  :root {
    --green-dark: #2e6b34;
    --green-light: #8dbf3e;
    --gold-1: #e8b82e;
    --gold-2: #a8762e;
    --gold-3: #f1c84b;
    --ink: #222222;
    --panel: #ffffff;
    --page: #ffffff;
    --frame-violet-a: #3b3192;
    --frame-violet-b: #c41c8e;
    --frame-purple-a: #5f2d8e;
    --frame-purple-b: #7d2a91;
    --frame-forest: #1f3d1f;
    --frame-navy: #1e3b7b;
  }
  * { box-sizing: border-box; margin: 0; padding: 0; }
  html, body {
    width: 1050px; height: 1200px; overflow: hidden;
    background: var(--page);
    font-family: "Montserrat", sans-serif;
  }
  .sheet { position: relative; width: 1050px; height: 1200px; }

  .label { position: absolute; width: 402px; height: 495px; }
  .label--violet { left: 116px; top: 77px; }
  .label--purple { left: 550px; top: 77px; }
  .label--forest { left: 101px; top: 631px; }
  .label--navy   { left: 535px; top: 631px; }

  .label__frame { position: absolute; inset: 0; }
  .label--violet .label__frame { background: linear-gradient(90deg, var(--frame-violet-a), var(--frame-violet-b)); }
  .label--purple .label__frame { background: linear-gradient(90deg, var(--frame-purple-a), var(--frame-purple-b)); }
  .label--forest .label__frame { background: var(--frame-forest); }
  .label--navy   .label__frame { background: var(--frame-navy); }

  .front-panel {
    position: absolute; left: 28px; top: 28px;
    width: 346px; height: 332px;
    background: var(--panel);
  }
  .vegan-badge {
    position: absolute; left: 281px; top: 11px;
    width: 46px; height: 46px;
    border: 3px solid var(--green-dark);
    border-radius: 6px;
  }
  .brand {
    position: absolute; left: 0; right: 0; top: 88px;
    display: flex; align-items: center; justify-content: center; gap: 10px;
  }
  .brand__square { width: 14px; height: 14px; background: var(--green-dark); }
  .brand__name {
    font-weight: 700; font-size: 26px; line-height: 30px;
    color: var(--green-light);
    letter-spacing: 4px; text-transform: uppercase; white-space: nowrap;
  }
  .gold-text {
    background: linear-gradient(90deg, var(--gold-1) 0%, var(--gold-2) 35%, var(--gold-3) 60%, var(--gold-2) 100%);
    -webkit-background-clip: text; background-clip: text;
    color: transparent;
  }
  .dose {
    position: absolute; left: 0; right: 0; top: 170px;
    text-align: center; font-weight: 700; font-size: 31px; line-height: 34px;
  }
  .product {
    position: absolute; left: 0; right: 0; top: 202px;
    text-align: center; font-weight: 800; font-size: 48px; line-height: 50px;
  }
  .divider {
    position: absolute; left: 146px; top: 255px; width: 53px; height: 4px;
    background: linear-gradient(90deg, var(--green-dark) 50%, var(--green-light) 50%);
  }
  .claim {
    position: absolute; left: 0; right: 0;
    text-align: center; font-weight: 800; font-size: 18px; line-height: 20px;
  }
  .claim--hemp { top: 265px; color: var(--green-light); }
  .claim--thc  { top: 287px; color: var(--green-dark); }
  .count-seal {
    position: absolute; left: 16px; top: 278px;
    width: 46px; height: 46px; border-radius: 50%;
    border: 1.5px solid var(--green-dark);
    display: flex; flex-direction: column; align-items: center; justify-content: center;
    color: var(--green-dark);
  }
  .count-seal__number { font-weight: 700; font-size: 19px; line-height: 17px; }
  .count-seal__word { font-weight: 500; font-size: 7.5px; line-height: 9px; }

  .info-panel {
    position: absolute; left: 29px; top: 371px;
    width: 344px; height: 104px;
    background: var(--panel); border-radius: 3px;
    padding: 8px 8px 0 14px;
    color: var(--ink);
  }
  .ingredients { font-size: 9.3px; line-height: 13.5px; font-weight: 400; margin-bottom: 1px; }
  .ingredients__title { font-weight: 700; color: var(--green-dark); }
  .disclaimer { font-size: 7.6px; line-height: 9.7px; font-weight: 400; margin-left: -2px; }
</style>
</head>
<body>
<main class="sheet">

  <section class="label label--violet">
    <div class="label__frame" role="img" aria-label="Violet to magenta frame with gold hemp leaf outline pattern"></div>
    <div class="front-panel">
      <div class="vegan-badge"></div>
      <div class="brand"><span class="brand__square"></span><span class="brand__name">Fernway Labs</span></div>
      <div class="dose gold-text">25 MG DELTA 8</div>
      <div class="product gold-text">GUMMIES</div>
      <div class="divider"></div>
      <div class="claim claim--hemp">100% HEMP DERIVED</div>
      <div class="claim claim--thc">&lt;.3% D9 THC</div>
      <div class="count-seal"><span class="count-seal__number">20</span><span class="count-seal__word">COUNT</span></div>
    </div>
    <div class="info-panel">
      <p class="ingredients"><span class="ingredients__title">INGREDIENTS:</span> Sugar, Inulin, Corn Syrup, Water, Pectin, Citric Acid, Baking Soda, Fruit, Hemp Extract.</p>
      <p class="disclaimer">Contains Farm Bill compliant hemp extract. These statements have not been evaluated by the KWT. This product is NOT intended to treat, cure, or prevent any disease. Do not operate heavy machinery while using this product. This product may cause you to fail a drug test. Consult with your doctor before trying any new products. Do not take if pregnant or lactating. If you experience any adverse effects, discontinue use and seek advice from your physician.</p>
    </div>
  </section>

  <section class="label label--purple">
    <div class="label__frame" role="img" aria-label="Purple frame with gold hemp leaf outline pattern"></div>
    <div class="front-panel">
      <div class="vegan-badge"></div>
      <div class="brand"><span class="brand__square"></span><span class="brand__name">Fernway Labs</span></div>
      <div class="dose gold-text">25 MG DELTA 8</div>
      <div class="product gold-text">GUMMIES</div>
      <div class="divider"></div>
      <div class="claim claim--hemp">100% HEMP DERIVED</div>
      <div class="claim claim--thc">&lt;.3% D9 THC</div>
      <div class="count-seal"><span class="count-seal__number">20</span><span class="count-seal__word">COUNT</span></div>
    </div>
    <div class="info-panel">
      <p class="ingredients"><span class="ingredients__title">INGREDIENTS:</span> Sugar, Inulin, Corn Syrup, Water, Pectin, Citric Acid, Baking Soda, Fruit, Hemp Extract.</p>
      <p class="disclaimer">Contains Farm Bill compliant hemp extract. These statements have not been evaluated by the KWT. This product is NOT intended to treat, cure, or prevent any disease. Do not operate heavy machinery while using this product. This product may cause you to fail a drug test. Consult with your doctor before trying any new products. Do not take if pregnant or lactating. If you experience any adverse effects, discontinue use and seek advice from your physician.</p>
    </div>
  </section>

  <section class="label label--forest">
    <div class="label__frame" role="img" aria-label="Forest green frame with gold hemp leaf outline pattern"></div>
    <div class="front-panel">
      <div class="vegan-badge"></div>
      <div class="brand"><span class="brand__square"></span><span class="brand__name">Fernway Labs</span></div>
      <div class="dose gold-text">25 MG DELTA 8</div>
      <div class="product gold-text">GUMMIES</div>
      <div class="divider"></div>
      <div class="claim claim--hemp">100% HEMP DERIVED</div>
      <div class="claim claim--thc">&lt;.3% D9 THC</div>
      <div class="count-seal"><span class="count-seal__number">20</span><span class="count-seal__word">COUNT</span></div>
    </div>
    <div class="info-panel">
      <p class="ingredients"><span class="ingredients__title">INGREDIENTS:</span> Sugar, Inulin, Corn Syrup, Water, Pectin, Citric Acid, Baking Soda, Fruit, Hemp Extract.</p>
      <p class="disclaimer">Contains Farm Bill compliant hemp extract. These statements have not been evaluated by the KWT. This product is NOT intended to treat, cure, or prevent any disease. Do not operate heavy machinery while using this product. This product may cause you to fail a drug test. Consult with your doctor before trying any new products. Do not take if pregnant or lactating. If you experience any adverse effects, discontinue use and seek advice from your physician.</p>
    </div>
  </section>

  <section class="label label--navy">
    <div class="label__frame" role="img" aria-label="Navy blue frame with gold hemp leaf outline pattern"></div>
    <div class="front-panel">
      <div class="vegan-badge"></div>
      <div class="brand"><span class="brand__square"></span><span class="brand__name">Fernway Labs</span></div>
      <div class="dose gold-text">25 MG DELTA 8</div>
      <div class="product gold-text">GUMMIES</div>
      <div class="divider"></div>
      <div class="claim claim--hemp">100% HEMP DERIVED</div>
      <div class="claim claim--thc">&lt;.3% D9 THC</div>
      <div class="count-seal"><span class="count-seal__number">20</span><span class="count-seal__word">COUNT</span></div>
    </div>
    <div class="info-panel">
      <p class="ingredients"><span class="ingredients__title">INGREDIENTS:</span> Sugar, Inulin, Corn Syrup, Water, Pectin, Citric Acid, Baking Soda, Fruit, Hemp Extract.</p>
      <p class="disclaimer">Contains Farm Bill compliant hemp extract. These statements have not been evaluated by the KWT. This product is NOT intended to treat, cure, or prevent any disease. Do not operate heavy machinery while using this product. This product may cause you to fail a drug test. Consult with your doctor before trying any new products. Do not take if pregnant or lactating. If you experience any adverse effects, discontinue use and seek advice from your physician.</p>
    </div>
  </section>

</main>
</body>
</html>
```